Tarvell homes and renovations business card design.

Would like some new card designs utilizing my new logo that look professional. I am open to different colors on the logo or utilize the same ones we have. I like the original concept but would like to see some fresh ideas and build on what we have already done.

Target Market(s)

Custom home building industry, Real estate sales, Renovation projects.

Industry/Entity Type

Home Builder

Contact Information for Business Card

Tarvell Homes and Renovations
2871 162nd Street
Brannock, Northvale
T0L3P0
Home : 403- 555-0187 Cell: 403- 555-0243

My info is : Gus Tarvell, President and CEO
email: tarvellhomes@quillmail.example
Website: tarvellhomes.example

Requirements
Must have
• Must Use my new logo design. I am open to different colors on the logo or utilize the same ones in the existing design. I can upload the original logo design if needed.

```html
<!DOCTYPE html>
<html lang="en">
<head>
<meta charset="utf-8">
<title>Tarvell Homes and Renovations – Business Card</title>
<link rel="stylesheet" href="https://fonts.googleapis.com/css2?family=Exo+2:wght@700;800&family=Open+Sans:wght@400;600&display=swap">
<style>
  :root {
    --stage: #1c1c1e;
    --card-white: #ffffff;
    --card-back-top: #f4f4f4;
    --card-back-bottom: #dcdcdc;
    --map-tone: #c9c9c9;
    --gold: #b98a2a;
    --gold-line: #e0b21f;
    --ink: #4a4a4a;
    --ink-soft: #6b6b6b;
  }
  * { box-sizing: border-box; margin: 0; padding: 0; }
  html, body {
    width: 1200px; height: 1000px; overflow: hidden;
    background: var(--stage);
    font-family: "Open Sans", Arial, sans-serif;
  }
  .canvas {
    position: relative; width: 1200px; height: 1000px;
    display: flex; flex-direction: column; align-items: center; justify-content: center; gap: 60px;
  }
  .card {
    position: relative; width: 700px; height: 400px; border-radius: 22px; overflow: hidden;
    box-shadow: 0 14px 40px rgba(0,0,0,.55);
  }
  /* Front */
  .card-front { background: var(--card-white); }
  .holder { position: absolute; left: 52px; top: 62px; }
  .holder-name {
    font-family: "Exo 2", "Arial Black", sans-serif; font-weight: 800;
    font-size: 34px; letter-spacing: 2px; color: var(--gold); line-height: 1;
  }
  .holder-title { font-size: 16px; color: var(--ink-soft); margin-top: 6px; }
  .rule {
    position: absolute; left: 300px; top: 90px; width: 360px; height: 2px; background: var(--gold-line);
  }
  .contact-list { position: absolute; left: 52px; top: 150px; list-style: none; }
  .contact-list li {
    display: flex; align-items: center; gap: 12px;
    font-size: 16px; color: var(--ink); line-height: 30px;
  }
  .contact-list svg { width: 14px; height: 14px; flex: none; }
  .web-accent { color: var(--gold); }
  .brand {
    position: absolute; right: 52px; top: 180px;
    display: flex; align-items: center; gap: 12px;
  }
  .brand-mark { width: 16px; height: 16px; background: var(--gold); flex: none; }
  .brand-name {
    font-family: "Open Sans", Arial, sans-serif; font-weight: 600;
    font-size: 22px; color: var(--gold); line-height: 1.15; max-width: 220px;
  }
  .address {
    position: absolute; right: 52px; bottom: 44px;
    font-size: 16px; color: var(--ink); line-height: 24px;
    display: flex; align-items: center; gap: 12px;
  }
  .address p { text-align: right; }
  .address svg { width: 16px; height: 18px; flex: none; }
  /* Back */
  .card-back { background: linear-gradient(160deg, var(--card-back-top), var(--card-back-bottom)); }
  .map-field {
    position: absolute; inset: 30px 40px;
    background: radial-gradient(ellipse at 50% 50%, var(--map-tone) 0%, rgba(201,201,201,0) 70%);
    opacity: .7; border-radius: 12px;
  }
  .back-brand {
    position: absolute; left: 0; right: 0; top: 150px;
    display: flex; justify-content: center; align-items: center; gap: 14px;
  }
  .back-brand .brand-name { font-size: 30px; max-width: none; }
  .back-brand .brand-mark { width: 20px; height: 20px; }
  .back-web {
    position: absolute; left: 0; right: 0; top: 250px;
    display: flex; justify-content: center; align-items: center; gap: 10px;
    font-size: 18px; color: var(--ink);
  }
  .back-web svg { width: 15px; height: 15px; }
</style>
</head>
<body>
<main class="canvas">
  <section class="card card-front" aria-label="Business card front">
    <div class="holder">
      <h1 class="holder-name">GUS TARVELL</h1>
      <p class="holder-title">President and CEO</p>
    </div>
    <div class="rule"></div>
    <ul class="contact-list">
      <li>
        <svg viewBox="0 0 14 14" aria-hidden="true"><path d="M3 1l2 3-1.5 1.5a8 8 0 0 0 5 5L10 9l3 2-1.5 2.5C6 13 1 8 .5 2.5z" fill="var(--gold)"/></svg>
        403 555 0187
      </li>
      <li>
        <svg viewBox="0 0 14 14" aria-hidden="true"><rect x="3.5" y="0.5" width="7" height="13" rx="1.5" fill="none" stroke="var(--gold)" stroke-width="1.4"/><circle cx="7" cy="11" r=".9" fill="var(--gold)"/></svg>
        403 555 0243
      </li>
      <li>
        <svg viewBox="0 0 14 14" aria-hidden="true"><rect x="0.5" y="2.5" width="13" height="9" fill="var(--gold)"/><path d="M.5 2.5L7 8l6.5-5.5" fill="none" stroke="#fff" stroke-width="1.2"/></svg>
        tarvellhomes@quillmail.example
      </li>
      <li>
        <svg viewBox="0 0 14 14" aria-hidden="true"><circle cx="8.5" cy="5.5" r="4" fill="none" stroke="var(--gold)" stroke-width="1.6"/><path d="M5.5 8.5L1 13" stroke="var(--gold)" stroke-width="2"/></svg>
        <span>www.<span class="web-accent">tarvellhomes</span>.example</span>
      </li>
    </ul>
    <div class="brand">
      <span class="brand-mark"></span>
      <span class="brand-name">Tarvell Homes and Renovations</span>
    </div>
    <div class="address">
      <svg viewBox="0 0 16 18" aria-hidden="true"><path d="M8 1C4.7 1 2 3.6 2 6.9 2 11 8 17 8 17s6-6 6-10.1C14 3.6 11.3 1 8 1z" fill="none" stroke="var(--gold)" stroke-width="1.6"/><circle cx="8" cy="7" r="2" fill="var(--gold)"/></svg>
      <p>2871 162nd Street<br>Brannock, Northvale</p>
    </div>
  </section>

  <section class="card card-back" aria-label="Business card back">
    <div class="map-field" role="img" aria-label="Faint world map background"></div>
    <div class="back-brand">
      <span class="brand-mark"></span>
      <span class="brand-name">Tarvell Homes and Renovations</span>
    </div>
    <p class="back-web">
      <svg viewBox="0 0 14 14" aria-hidden="true"><circle cx="8.5" cy="5.5" r="4" fill="none" stroke="var(--gold)" stroke-width="1.6"/><path d="M5.5 8.5L1 13" stroke="var(--gold)" stroke-width="2"/></svg>
      <span>www.<span class="web-accent">tarvellhomes</span>.example</span>
    </p>
  </section>
</main>
</body>
</html>
```